Business Card Design for Kidvale (Hires out childrens play areas)

Looking to have a business card designed for a company we just bought. The company rents out childrens play areas.

I have uploaded a couple of examples of the kind of business card style I like. Here are two more examples:

https://quorvastudio.nz/project/bright-romp-branding/
https://imgvaultcdn.com/design_img/8841052/302917/302917_5518203_8841052_b73e19a2_image.jpg

I think a white card will be best due to all the colours in the logo.

Size we require: 3.75" x 2.25" (horizontally orientated) with a 0.125" bleed

Uploaded is two versions of our logo.

Details for the card:
1. My name: Liam Verster
2. Title: Managing Director
3. Phone no: 021 563 417
4. Email: liam@kidvale.co.nz
5. URL: www.kidvale.co.nz
6. Address:
PO Box 318625
Fernlea, Auckland

Let me know if you need anything else.

Target Market(s)

Hospitals, doctors surgeries, bed shops, etc.

Contact Information for Business Card

Details for the card:
1. My name: Liam Verster
3. Phone no: 021 563 417
5. URL: www.kidvale.co.nz
6. Address:
PO Box 318625
Fernlea, Auckland

Requirements
Should not have
• Not too busy.

```html
<!DOCTYPE html>
<html lang="en">
<head>
<meta charset="utf-8">
<title>Kidvale Business Card</title>
<link rel="stylesheet" href="https://fonts.googleapis.com/css2?family=Quicksand:wght@500;600;700&display=swap">
<style>
  :root {
    --stage: #2b2d31;
    --card-white: #ffffff;
    --brand-blue: #1a5fb4;
    --brand-orange: #f7941d;
    --text-grey: #4a4a4a;
    --stripe-teal: #1aa3a8;
    --stripe-red: #e2252b;
    --stripe-green: #3aaa48;
    --stripe-orange: #f7941d;
    --back-light: #f9a825;
    --back-deep: #ec5a22;
    --mascot-purple: #8e2fb5;
    --mascot-pink: #e0359a;
  }
  * { box-sizing: border-box; margin: 0; padding: 0; }
  html, body {
    width: 1200px; height: 900px; overflow: hidden;
    background: var(--stage);
    font-family: "Quicksand", sans-serif;
  }
  .sheet {
    position: relative; width: 1200px; height: 900px;
  }
  .card {
    position: absolute; left: 290px;
    width: 620px; height: 372px;
    border-radius: 24px; overflow: hidden;
  }
  /* Front */
  .card-front { top: 60px; background: var(--card-white); }
  .name-band {
    position: absolute; left: 0; right: 0; top: 78px; height: 64px;
    background: var(--brand-blue);
  }
  .holder-name {
    position: absolute; left: 62px; top: 80px;
    font-size: 32px; font-weight: 600; color: var(--brand-orange);
    line-height: 1.1;
  }
  .holder-title {
    position: absolute; left: 64px; top: 116px;
    font-size: 15px; font-weight: 500; color: var(--card-white);
  }
  .mascot-ring {
    position: absolute; left: 352px; top: 64px;
    width: 176px; height: 176px; border-radius: 50%;
    background: var(--card-white);
  }
  .mascot-area {
    position: absolute; left: 366px; top: 78px;
    width: 148px; height: 148px; border-radius: 50%;
    background: radial-gradient(circle at 40% 35%, var(--mascot-pink), var(--mascot-purple));
  }
  .contact-list {
    position: absolute; left: 62px; top: 172px;
    list-style: none; font-size: 15px; font-weight: 500;
    color: var(--text-grey); line-height: 1.45;
  }
  .postal-address {
    position: absolute; right: 44px; bottom: 46px;
    text-align: right; font-style: normal;
    font-size: 18px; font-weight: 500; color: var(--text-grey);
    line-height: 1.35;
  }
  .colour-stripe {
    position: absolute; left: 0; right: 0; bottom: 0; height: 20px;
    display: flex;
  }
  .colour-stripe span { flex: 1; }
  .stripe-teal { background: var(--stripe-teal); }
  .stripe-red { background: var(--stripe-red); }
  .stripe-green { background: var(--stripe-green); }
  .stripe-orange { background: var(--stripe-orange); }
  /* Back */
  .card-back {
    top: 468px;
    background: radial-gradient(ellipse at 50% 50%, var(--back-light) 0%, var(--back-deep) 85%);
    display: flex; align-items: center; justify-content: center;
  }
  .brand-name {
    font-size: 72px; font-weight: 700; color: var(--card-white);
    letter-spacing: 1px;
  }
</style>
</head>
<body>
<main class="sheet">
  <section class="card card-front" aria-label="Business card front">
    <div class="name-band"></div>
    <h1 class="holder-name">Liam Verster</h1>
    <p class="holder-title">Managing Director</p>
    <div class="mascot-ring"></div>
    <div class="mascot-area" role="img" aria-label="Kidvale mascot illustration of a smiling child"></div>
    <ul class="contact-list">
      <li>021 563 417</li>
      <li>liam@kidvale.co.nz</li>
      <li>www.kidvale.co.nz</li>
    </ul>
    <address class="postal-address">PO Box 318625<br>Fernlea, Auckland</address>
    <div class="colour-stripe">
      <span class="stripe-teal"></span>
      <span class="stripe-red"></span>
      <span class="stripe-green"></span>
      <span class="stripe-orange"></span>
    </div>
  </section>
  <section class="card card-back" aria-label="Business card back">
    <p class="brand-name">Kidvale</p>
  </section>
</main>
</body>
</html>
```